Front Yard Sign for Real Estate Company

Bright Door Homes is a brand new real estate broker. We need signs to put in front yard of houses that we are selling. 3D would be great. I have included the company LOGO

Target Market(s)

Residential Property buyers and sellers

Industry/Entity Type

Real Estate

Colors
ec1f27
ffc214
fbed22
ffffff

Requirements
Must have
• 3D look would be great. Logo must be included in the yard signs.
• Must include phone # to call: 555-214-6073

```html
<!DOCTYPE html>
<html lang="en">
<head>
<meta charset="utf-8">
<title>Bright Door Homes – For Sale Yard Sign</title>
<link rel="stylesheet" href="https://fonts.googleapis.com/css2?family=Anton&family=Montserrat:wght@700;800&display=swap">
<style>
  :root {
    --brand-red: #ec1f27;
    --deep-red: #9a0910;
    --sign-yellow: #fbd214;
    --sign-gold: #ffc214;
    --extrude-light: #f5a01e;
    --extrude-dark: #e2621b;
    --band-white: #ffffff;
  }
  html, body {
    margin: 0;
    padding: 0;
    width: 1200px;
    height: 1030px;
    overflow: hidden;
    background: var(--band-white);
  }
  .yard-sign {
    display: block;
    width: 1200px;
    height: 1030px;
  }
  .headline {
    font-family: "Anton", "Oswald", sans-serif;
    font-size: 292px;
  }
  .brand-name {
    font-family: "Montserrat", sans-serif;
    font-weight: 800;
    font-size: 26px;
    fill: var(--brand-red);
  }
  .phone-number {
    font-family: "Montserrat", sans-serif;
    font-weight: 700;
    font-size: 80px;
    letter-spacing: 6px;
    fill: var(--brand-red);
  }
</style>
</head>
<body>
<svg class="yard-sign" viewBox="0 0 1200 1030" xmlns="http://www.w3.org/2000/svg" role="img" aria-label="For Sale yard sign for Bright Door Homes, call 555-214-6073">
  <defs>
    <linearGradient id="sky-red" x1="0" y1="0" x2="0" y2="1">
      <stop offset="0" stop-color="var(--deep-red)"/>
      <stop offset="0.75" stop-color="var(--brand-red)"/>
      <stop offset="1" stop-color="var(--brand-red)"/>
    </linearGradient>
    <linearGradient id="face-yellow" x1="0" y1="0" x2="0" y2="1">
      <stop offset="0" stop-color="var(--sign-yellow)"/>
      <stop offset="1" stop-color="var(--sign-gold)"/>
    </linearGradient>
    <linearGradient id="depth-orange" x1="0" y1="0" x2="0" y2="1">
      <stop offset="0" stop-color="var(--extrude-light)"/>
      <stop offset="1" stop-color="var(--extrude-dark)"/>
    </linearGradient>
    <filter id="soft-shadow" x="-10%" y="-10%" width="120%" height="140%">
      <feGaussianBlur stdDeviation="8"/>
    </filter>
    <text id="for-sale-word" class="headline" x="65" y="606" textLength="995" lengthAdjust="spacingAndGlyphs">FOR SALE</text>
  </defs>

  <rect class="sign-field" x="0" y="0" width="1200" height="780" fill="url(#sky-red)"/>

  <use href="#for-sale-word" transform="translate(0 1290) scale(1 -1.05)" fill="#8f0c12" opacity="0.35"/>
  <use href="#for-sale-word" transform="translate(20 14)" fill="#5a0206" opacity="0.45" filter="url(#soft-shadow)"/>

  <g class="headline-depth" fill="url(#depth-orange)">
    <use href="#for-sale-word" transform="translate(75 -60)"/>
    <use href="#for-sale-word" transform="translate(70 -56)"/>
    <use href="#for-sale-word" transform="translate(65 -52)"/>
    <use href="#for-sale-word" transform="translate(60 -48)"/>
    <use href="#for-sale-word" transform="translate(55 -44)"/>
    <use href="#for-sale-word" transform="translate(50 -40)"/>
    <use href="#for-sale-word" transform="translate(45 -36)"/>
    <use href="#for-sale-word" transform="translate(40 -32)"/>
    <use href="#for-sale-word" transform="translate(35 -28)"/>
    <use href="#for-sale-word" transform="translate(30 -24)"/>
    <use href="#for-sale-word" transform="translate(25 -20)"/>
    <use href="#for-sale-word" transform="translate(20 -16)"/>
    <use href="#for-sale-word" transform="translate(15 -12)"/>
    <use href="#for-sale-word" transform="translate(10 -8)"/>
    <use href="#for-sale-word" transform="translate(5 -4)"/>
  </g>

  <use class="headline-face" href="#for-sale-word" fill="url(#face-yellow)"/>

  <path class="contact-band" d="M0 778 H96 L187 720 L278 778 H1200 V1030 H0 Z" fill="var(--band-white)"/>

  <g class="brand">
    <circle cx="60" cy="909" r="10" fill="var(--brand-red)"/>
    <text class="brand-name" x="78" y="918" textLength="250" lengthAdjust="spacingAndGlyphs">Bright Door Homes</text>
  </g>

  <g class="phone">
    <circle cx="416" cy="897" r="44" fill="var(--brand-red)"/>
    <path d="M402 874 c-5 3 -8 7 -7 13 c2 14 16 32 30 38 c5 2 10 1 14 -3 l3 -3 c2 -2 2 -5 0 -7 l-7 -6 c-2 -2 -5 -2 -7 0 l-3 3 c-7 -3 -13 -10 -16 -17 l3 -3 c2 -2 2 -5 1 -7 l-5 -8 c-2 -2 -4 -2 -6 0 z" fill="var(--band-white)"/>
    <text class="phone-number" x="488" y="926" textLength="642" lengthAdjust="spacing">555-214-6073</text>
  </g>
</svg>
</body>
</html>
```